Brightwire Hollow Business cards

one side I would like my logo (uploaded) and the other side I want my details. I'm an electrician in sydney. The logo side I'm happy with just a white background and our logo in the middle.

Details for other side
24/7 Sydney Electrician
Marcus Pell
0431 587 219
marcus@brightwirehollow.com.au
brightwirehollow.com.au
icons for facebook, instagram, linked in

Industry/Entity Type

electrician

Contact Information for Business Card

company info

```html
<!DOCTYPE html>
<html lang="en">
<head>
<meta charset="utf-8">
<title>Brightwire Hollow – Business Cards</title>
<link rel="stylesheet" href="https://fonts.googleapis.com/css2?family=Montserrat:wght@400;500;700;800&display=swap">
<style>
  :root {
    --backdrop: #1b1b1b;
    --card-dark: #202020;
    --card-light: #f3f3f3;
    --brand-red: #e1301f;
    --ink-light: #f4f4f4;
    --ink-dark: #222222;
  }
  * { box-sizing: border-box; margin: 0; padding: 0; }
  html, body {
    width: 1200px; height: 1059px; overflow: hidden;
    background: var(--backdrop);
    font-family: "Montserrat", Arial, sans-serif;
  }
  .canvas { position: relative; width: 1200px; height: 1059px; }

  .card {
    position: absolute;
    border-radius: 16px;
    overflow: hidden;
  }
  .card--details {
    left: 299px; top: 89px; width: 603px; height: 390px;
    background: var(--card-dark);
  }
  .card--brand {
    left: 295px; top: 547px; width: 611px; height: 394px;
    background: var(--card-light);
  }

  .wordmark {
    position: absolute;
    color: var(--brand-red);
    font-weight: 800;
    text-transform: uppercase;
    line-height: 0.98;
    letter-spacing: 0.02em;
  }
  .card--details .wordmark {
    right: 36px; top: 46px;
    font-size: 34px;
    text-align: right;
  }
  .card--brand .wordmark {
    left: 0; right: 0; top: 132px;
    font-size: 54px;
    text-align: center;
  }

  .holder-name {
    position: absolute; left: 35px; top: 210px;
    color: var(--brand-red);
    font-size: 28px; font-weight: 700;
    letter-spacing: 0.04em;
    text-transform: uppercase;
  }
  .divider {
    position: absolute; left: 35px; right: 36px; top: 259px;
    height: 1.5px; background: var(--brand-red);
  }
  .contact-list {
    position: absolute; left: 38px; top: 275px;
    list-style: none;
  }
  .contact-list li {
    display: flex; align-items: center; gap: 8px;
    height: 27.5px;
    color: var(--ink-light);
    font-size: 17.5px; font-weight: 400;
    letter-spacing: 0.02em;
  }
  .contact-list svg { width: 11px; height: 11px; flex: none; fill: var(--brand-red); }

  .service-area {
    position: absolute; right: 36px; top: 330px;
    display: flex; align-items: center; gap: 5px;
    color: var(--ink-light);
    font-size: 17.5px; font-weight: 400;
    letter-spacing: 0.02em;
  }
  .service-area svg { width: 10px; height: 14px; fill: var(--brand-red); }

  .social-row {
    position: absolute; left: 0; right: 0; top: 326px;
    display: flex; justify-content: center; align-items: center; gap: 6px;
  }
  .social-row .rule { width: 78px; height: 1.5px; background: var(--brand-red); margin: 0 5px; }
  .social-dot {
    width: 22px; height: 22px; border-radius: 50%;
    background: var(--brand-red);
  }
</style>
</head>
<body>
<main class="canvas">

  <section class="card card--details" aria-label="Business card, details side">
    <div class="wordmark">Brightwire<br>Hollow</div>

    <h1 class="holder-name">Marcus Pell</h1>
    <div class="divider"></div>

    <ul class="contact-list">
      <li>
        <svg viewBox="0 0 12 12" aria-hidden="true"><path d="M1 4c0-2 2-3 5-3s5 1 5 3l-2 1-1-1H4L3 5 1 4zm2 2h6l1 5H2l1-5zm3 1a1.5 1.5 0 100 3 1.5 1.5 0 000-3z"/></svg>
        0431 587 219
      </li>
      <li>
        <svg viewBox="0 0 12 12" aria-hidden="true"><path d="M0 5l6-4 6 4v6H0V5zm1 1v4l3-2-3-2zm10 0L8 8l3 2V6zM2 11h8L6 8.5 2 11z"/></svg>
        marcus@brightwirehollow.com.au
      </li>
      <li>
        <svg viewBox="0 0 12 12" aria-hidden="true"><path d="M6 0a6 6 0 110 12A6 6 0 016 0zM3 2.5C2 3.5 1.5 5 2 6.5l2 .5 1 2 1-1-1-2 1-1-1-2H3zm5-.5L7 3.5l1.5 1.5L10 4 8 2zm1 5l-1.5 1L8 10a4.5 4.5 0 002-3H9z"/></svg>
        brightwirehollow.com.au
      </li>
    </ul>

    <div class="service-area">
      24/7 Sydney Electrician
      <svg viewBox="0 0 10 14" aria-hidden="true"><path d="M5 0a5 5 0 015 5c0 3.5-5 9-5 9S0 8.5 0 5a5 5 0 015-5zm0 3a2 2 0 100 4 2 2 0 000-4z"/></svg>
    </div>
  </section>

  <section class="card card--brand" aria-label="Business card, brand side">
    <div class="wordmark">Brightwire<br>Hollow</div>

    <div class="social-row" aria-label="Social media links">
      <span class="rule"></span>
      <span class="social-dot" role="img" aria-label="Social profile link one"></span>
      <span class="social-dot" role="img" aria-label="Social profile link two"></span>
      <span class="social-dot" role="img" aria-label="Social profile link three"></span>
      <span class="rule"></span>
    </div>
  </section>

</main>
</body>
</html>
```